Velmora glow cosmetic line

The name of the brand would be Velmora Glow. Natural products for à never aging skin.
We produce natural home made skin care products with African products.
Our target market is the affluent African and diaspora looking for that natural glowing skin that respect nature and their skin complexion

Target Market(s)

Affluent African and diaspora

Industry/Entity Type

Skin Care Product

Font styles to use
Sans Serif

Colors

Designer to choose colors to be used in the design.

Requirements
Must have
• Nature touch and African touch

```html
<!DOCTYPE html>
<html lang="en">
<head>
<meta charset="UTF-8">
<title>Velmora Glow – Anti-Aging Cream Label</title>
<link rel="stylesheet" href="https://fonts.googleapis.com/css2?family=Lato:wght@400;700&family=Dancing+Script:wght@500&display=swap">
<style>
  :root {
    --backdrop: #5a5a5a;
    --label-paper: #fbfbfa;
    --pattern-tint: #f1eef0;
    --gold-rule: #c9a55a;
    --ink: #2b2b2b;
    --teal: #1f9e8a;
    --teal-light: #5fc0b0;
    --band-text: #ffffff;
    --mark-green: #6b9a5a;
  }
  * { margin: 0; padding: 0; box-sizing: border-box; }
  html, body {
    width: 1200px;
    height: 800px;
    overflow: hidden;
    background: var(--backdrop);
  }
  .canvas {
    position: relative;
    width: 1200px;
    height: 800px;
  }
  .label {
    position: absolute;
    left: 100px;
    top: 103px;
    width: 1000px;
    height: 594px;
    background: var(--label-paper);
    overflow: hidden;
  }
  .label-pattern {
    position: absolute;
    inset: 0;
    background: radial-gradient(circle at 50% 50%, var(--label-paper) 0%, var(--pattern-tint) 100%);
  }
  .gold-rule {
    position: absolute;
    left: 0;
    width: 100%;
    height: 3px;
    background: var(--gold-rule);
  }
  .gold-rule.top { top: 26px; }
  .gold-rule.bottom { top: 570px; }
  .brand-mark {
    position: absolute;
    top: 82px;
    left: 0;
    width: 100%;
    display: flex;
    justify-content: center;
    align-items: center;
    gap: 12px;
    font-family: "Lato", sans-serif;
    font-size: 26px;
    color: var(--mark-green);
  }
  .brand-mark .dot {
    width: 22px;
    height: 22px;
    border-radius: 50%;
    background: var(--mark-green);
  }
  .brand-name {
    position: absolute;
    top: 212px;
    width: 100%;
    text-align: center;
    font-family: "Lato", sans-serif;
    font-weight: 400;
    font-size: 50px;
    letter-spacing: 1px;
    text-transform: uppercase;
    color: var(--ink);
  }
  .product-band {
    position: absolute;
    left: 237px;
    top: 300px;
    width: 526px;
    height: 134px;
  }
  .product-band svg { position: absolute; inset: 0; }
  .product-type {
    position: absolute;
    inset: 0;
    display: flex;
    align-items: center;
    justify-content: center;
    font-family: "Lato", sans-serif;
    font-size: 54px;
    color: var(--band-text);
  }
  .tagline {
    position: absolute;
    top: 446px;
    width: 100%;
    text-align: center;
    font-family: "Lato", sans-serif;
    font-size: 50px;
    color: var(--ink);
  }
  .origin-note {
    position: absolute;
    top: 510px;
    width: 100%;
    text-align: center;
    font-family: "Dancing Script", cursive;
    font-size: 32px;
    color: var(--ink);
  }
</style>
</head>
<body>
  <main class="canvas">
    <section class="label">
      <div class="label-pattern" role="img" aria-label="Faint pale floral pattern across the label paper"></div>
      <div class="gold-rule top"></div>

      <div class="brand-mark">
        <span class="dot"></span>
        <span>Velmora Glow</span>
      </div>

      <h1 class="brand-name">Velmora Glow</h1>

      <div class="product-band">
        <svg width="526" height="134" viewBox="0 0 526 134">
          <rect x="0" y="0" width="526" height="4" fill="var(--teal-light)"/>
          <rect x="0" y="10" width="526" height="114" fill="var(--teal)"/>
          <rect x="0" y="130" width="526" height="4" fill="var(--teal-light)"/>
        </svg>
        <p class="product-type">anti-aging cream</p>
      </div>

      <p class="tagline">natural glowing skin</p>
      <p class="origin-note">home made product</p>

      <div class="gold-rule bottom"></div>
    </section>
  </main>
</body>
</html>
```